Flyer für ambulante und teilstationäre Pflege
Zielgruppe
ambulante und teilstationäre Pflege
Zielgruppe: Pflegebedürftige Menschen, die noch ausreichend mobil sind, um als Gast in unserer Tagespflege zu sein
Aufgabenstellung
Standard DIN lang Format
Stil soll unserer Homepage folgen: www.pflegeteam-sonnhalde.de
Wir achten immer sehr darauf, nicht so einen verstaubten Stil wie viele andere Pflegeeinrichtungen zu haben, sondern fröhlich, bunt , ansprechend

```html
<!DOCTYPE html>
<html lang="de">
<head>
<meta charset="utf-8">
<title>Flyer Pflegeteam Sonnhalde</title>
<link href="https://fonts.googleapis.com/css2?family=Merriweather:wght@900&family=Poppins:ital,wght@0,400;0,500;0,600;0,700;0,800;1,700&display=swap" rel="stylesheet">
<style>
:root{
  --red:#931a20;
  --teal:#2f968e;
  --teal-light:#5cb5ae;
  --black:#0b0b0b;
  --white:#ffffff;
  --ink:#1a1a1a;
  --grey:#555;
  --stage:#a3a3a3;
  --pink:#d9a7b8;
}
*{margin:0;padding:0;box-sizing:border-box}
html,body{width:1200px;height:1117px;overflow:hidden;background:var(--stage);font-family:'Poppins',sans-serif}
.page{position:absolute;top:183px;width:531px;height:751px;background:var(--white);overflow:hidden}
.page--front{left:58px}
.page--back{left:610px}
.shapes{position:absolute;inset:0;width:531px;height:751px}

/* front */
.brand{position:absolute;top:24px;display:flex;align-items:center;gap:6px;font-family:'Poppins',sans-serif;font-weight:500;color:var(--grey);text-transform:uppercase;line-height:1.15;white-space:nowrap}
.brand__text{display:flex;flex-direction:column}
.brand__name{font-size:11.5px;letter-spacing:.1px}
.brand__sub{font-size:7.5px;text-align:right}
.brand__dot{flex:none;width:30px;height:30px;border-radius:50%}
.brand--day{left:45px}
.brand--day .brand__dot{background:var(--teal)}
.brand--mobile{left:275px}
.brand--mobile .brand__dot{background:var(--red)}
.brand-divider{position:absolute;left:264px;top:18px;width:1px;height:44px;background:#bbb}
.headline{position:absolute;left:46px;top:96px;font-family:'Merriweather',serif;font-weight:900;font-size:30px;line-height:30px;color:var(--ink)}
.headline em{font-style:normal;color:var(--red)}
.welcome{position:absolute;left:45px;top:223px;font-size:10.5px;font-weight:600;line-height:13px;color:var(--ink)}
.intro{position:absolute;left:57px;top:282px;width:450px;font-size:10px;font-weight:600;line-height:12px;color:var(--white)}
.intro p+p{margin-top:11px}
.merits{position:absolute;left:296px;top:420px;width:215px}
.merits__title{font-size:15.5px;font-weight:700;line-height:16.5px;color:var(--white);text-align:right}
.merit{position:absolute;left:-2px;display:flex;align-items:center;width:230px}
.merit__icon{flex:none;width:40px;height:40px;border:2px solid var(--white);border-radius:50%;display:flex;align-items:center;justify-content:center}
.merit__text{margin-left:12px;font-size:11px;line-height:12.5px;color:var(--white)}
.url{position:absolute;left:172px;top:707px;font-size:15px;font-weight:700;color:var(--white)}
.url span{color:var(--pink)}

/* back */
.back-title{position:absolute;left:38px;top:256px;font-size:21.5px;font-weight:800;line-height:24px;color:var(--red)}
.back-lead{position:absolute;left:38px;top:364px;width:220px;font-size:15.5px;font-weight:700;line-height:17.5px;color:var(--white)}
.back-copy{position:absolute;left:295px;top:187px;width:210px;font-size:8.7px;line-height:10.3px;color:var(--ink)}
.back-copy p+p{margin-top:10px}
.quote{position:absolute;left:40px;top:541px;width:330px;font-size:9.6px;font-weight:700;font-style:italic;line-height:12px;color:var(--white)}
.quote cite{display:block;margin-top:8px;font-size:12.5px;font-style:italic}
.claim{position:absolute;left:0;top:646px;width:531px;text-align:center;font-size:10.4px;font-weight:600;line-height:12.5px;color:var(--white)}
.contacts{position:absolute;top:682px;font-size:9.6px;line-height:16.5px;color:var(--white)}
.contacts li{list-style:none;display:flex;align-items:flex-start;gap:6px}
.contacts svg{flex:none;margin-top:4px}
.contacts--left{left:47px}
.contacts--right{left:262px;line-height:11px}
.contacts--right li+li{margin-top:11px}
.contacts--right svg{margin-top:1px}
.contact-divider{position:absolute;left:248px;top:682px;width:1px;height:46px;background:var(--white)}
</style>
</head>
<body>

<section class="page page--front">
  <svg class="shapes" viewBox="0 0 531 751">
    <defs>
      <linearGradient id="warmPhoto" x1="0" y1="0" x2="1" y2="1">
        <stop offset="0" stop-color="#b89a8c"/><stop offset="1" stop-color="#e9ddd6"/>
      </linearGradient>
      <linearGradient id="outdoorPhoto" x1="0" y1="0" x2="1" y2="1">
        <stop offset="0" stop-color="#6d6a66"/><stop offset=".5" stop-color="#4a5060"/><stop offset="1" stop-color="#8c8378"/>
      </linearGradient>
    </defs>
    <rect role="img" aria-label="Foto: Pflegerin liest einer älteren Dame lachend aus einem Buch vor" x="340" y="73" width="191" height="170" fill="url(#warmPhoto)" opacity=".55"/>
    <path d="M313 75 A140 140 0 0 0 276 140" fill="none" stroke="var(--teal)" stroke-width="14"/>
    <path d="M276 140 A140 140 0 0 0 330 295" fill="none" stroke="var(--teal)" stroke-width="2"/>
    <path d="M325 268 A128 128 0 0 0 531 290 L531 300 A138 138 0 0 1 320 280 Z" fill="var(--teal)"/>
    <circle role="img" aria-label="Foto: Pflegerin liest einer älteren Dame lachend aus einem Buch vor" cx="408" cy="178" r="124" fill="url(#warmPhoto)"/>
    <rect role="img" aria-label="Foto: Betreuerin und zwei ältere Herren schauen draußen lachend auf ein Tablet" x="0" y="345" width="531" height="406" fill="url(#outdoorPhoto)"/>
    <polygon points="33,263 316,263 531,275 531,411 42,387" fill="var(--red)"/>
    <polygon points="277,389 531,411 531,680 277,665" fill="var(--teal)"/>
    <polygon points="0,650 531,689 531,698 0,659" fill="var(--white)"/>
    <polygon points="0,661 531,701 531,751 0,751" fill="var(--black)"/>
    <circle cx="72" cy="698" r="75" fill="var(--white)"/>
  </svg>

  <div class="brand brand--day">
    <div class="brand__text">
      <span class="brand__name">Tagespflege am Lindenhof</span>
      <span class="brand__sub">Lindenau</span>
    </div>
    <span class="brand__dot"></span>
  </div>
  <div class="brand-divider"></div>
  <div class="brand brand--mobile">
    <div class="brand__text">
      <span class="brand__name">Ambulante Krankenpflege</span>
      <span class="brand__sub">Sonnhalde - Lindenau - Birkwald</span>
    </div>
    <span class="brand__dot"></span>
  </div>

  <h1 class="headline">Von Mensch<br>zu Mensch -<br><em>Pflegeprofis<br>seit 1994</em></h1>
  <p class="welcome">Herzlich Willkommen bei der Ambulanten<br>Krankenpflege Sonnhalde &amp; Lindenau</p>

  <div class="intro">
    <p>Seit fast 30 Jahren sind wir nun schon Ihr Experte<br>für häusliche Pflege und Demenzbetreuung.<br>Ihr persönliches Wohl und das Ihrer Angehörigen liegt<br>uns am Herzen,</p>
    <p>Lassen Sie sich von uns in Ihrem Alltag behilflich sein und machen Sie noch heute einen Beratungstermin zu unseren Dienstleistungen mit einem unserer kompetenten Ansprechpartner.</p>
  </div>

  <div class="merits">
    <h2 class="merits__title">Was unseren Pflegedienst<br>auszeichnet</h2>
    <div class="merit" style="top:34px">
      <span class="merit__icon"><svg width="22" height="20" viewBox="0 0 22 20" fill="#fff"><circle cx="11" cy="7" r="3"/><circle cx="4.5" cy="9" r="2.3"/><circle cx="17.5" cy="9" r="2.3"/><path d="M6 19c0-4 2-7 5-7s5 3 5 7z"/><path d="M0 19c0-3 1.5-5.5 4.5-5.5 1 0 1.6.3 1.6.3C5 15 4.6 17 4.6 19z"/><path d="M22 19c0-3-1.5-5.5-4.5-5.5-1 0-1.6.3-1.6.3 1.1 1.2 1.5 3.2 1.5 5.2z"/></svg></span>
      <span class="merit__text">Über 25 Jahre Erfahrung</span>
    </div>
    <div class="merit" style="top:81px">
      <span class="merit__icon"><svg width="16" height="20" viewBox="0 0 16 20" fill="none" stroke="#fff" stroke-width="1.8"><path d="M2 1h8l4 4v14H2z"/><path d="M5 9h6M5 12h6M5 15h4"/></svg></span>
      <span class="merit__text">Abgestimmtes<br>Versorgungskonzept mit<br>Beratung zur Finanzierung</span>
    </div>
    <div class="merit" style="top:131px">
      <span class="merit__icon"><svg width="18" height="22" viewBox="0 0 18 22" fill="none" stroke="#fff" stroke-width="1.8"><circle cx="9" cy="8" r="6.5"/><circle cx="9" cy="8" r="3" fill="#fff"/><path d="M5 13l-2 8 3-2 2 2 1-5M13 13l2 8-3-2-2 2-1-5"/></svg></span>
      <span class="merit__text">Sehr gute MDK geprüfte<br>Pflegequalität auf höchstem<br>Niveau</span>
    </div>
    <div class="merit" style="top:179px">
      <span class="merit__icon"><svg width="18" height="20" viewBox="0 0 18 20" fill="none" stroke="#fff" stroke-width="1.8"><path d="M4 1h9l4 4v14H4z"/><path d="M8 8h6M8 11h6M10 14h4"/><circle cx="4.5" cy="14.5" r="3.5" fill="var(--teal)"/><path d="M3 14.5l1.2 1.2 2-2.2"/></svg></span>
      <span class="merit__text">Zulassung und<br>Versorgungsvertrag mit allen<br>Kranken- und Pflegekassen</span>
    </div>
  </div>

  <p class="url">www.<span>pflegeteam-sonnhalde</span>.de</p>
</section>

<section class="page page--back">
  <svg class="shapes" viewBox="0 0 531 751">
    <defs>
      <linearGradient id="loungePhoto" x1="0" y1="0" x2="1" y2="1">
        <stop offset="0" stop-color="#a58a74"/><stop offset=".5" stop-color="#8c5d7a"/><stop offset="1" stop-color="#c7b6b9"/>
      </linearGradient>
      <linearGradient id="snackPhoto" x1="0" y1="0" x2="1" y2="1">
        <stop offset="0" stop-color="#6f8fd0"/><stop offset=".6" stop-color="#d7dff0"/><stop offset="1" stop-color="#b4542a"/>
      </linearGradient>
      <linearGradient id="redShade" x1="0" y1="0" x2="1" y2="0">
        <stop offset="0" stop-color="var(--red)"/><stop offset=".5" stop-color="#a3262c"/><stop offset="1" stop-color="var(--red)"/>
      </linearGradient>
    </defs>
    <polygon role="img" aria-label="Foto: Tagesgäste sitzen in Sesseln im hellen Aufenthaltsraum" points="0,0 531,0 531,166 0,206" fill="url(#loungePhoto)"/>
    <circle cx="138" cy="133" r="116" fill="var(--white)"/>
    <circle role="img" aria-label="Foto: Brezeln und Weißwurst auf einer blau-weiß karierten Serviette" cx="138" cy="133" r="110" fill="url(#snackPhoto)"/>
    <polygon points="0,360 265,335 265,494 0,522" fill="var(--teal)"/>
    <polygon points="0,520 531,475 531,583 0,635" fill="url(#redShade)"/>
    <polygon points="0,635 531,583 531,751 0,751" fill="var(--black)"/>
    <circle cx="437" cy="560" r="62" fill="var(--white)"/>
  </svg>

  <h2 class="back-title">Abwechslungsreiche<br>Beschäftigung in der<br>Tagespflege</h2>
  <p class="back-lead">Besonders für Demenzkranke ist unsere stimulierende Tagespflege nicht einfach nur zweckmäßig, sondern spricht die Sinne an und lädt zum Verweilen ein.</p>

  <div class="back-copy">
    <p>Seit dem 15.01.2019 besitzen wir eine teilstationäre Tagespflegeeinrichtung mit 16 Plätzen im Gesundheitszentrum Lindenau. So können wir Ihnen auf einer Fläche von 243 m² mit Sonnenterrasse in gemütlicher Atmosphäre noch mehr Unterstützung anbieten.</p>
    <p>Bei uns können Sie sich auf eine abwechslungsreiche Betreuung und Beschäftigung an 5 Tagen der Woche freuen, die stets am Bedarf und den Vorlieben unserer Tagesgäste orientiert ist.</p>
    <p>Während Ihres Aufenthalts erhalten Sie professionelle medizinische und pflegerische Versorgung.</p>
    <p>In netter Gesellschaft können Sie soziale Kontakte knüpfen oder aufrechterhalten. Falls Sie doch einmal Ruhe benötigen, gibt es selbstverständlich Rückzugsmöglichkeiten.</p>
    <p>Nach Bedarf bieten wir Frühstück, selbst gekochtes Mittagessen, Nachmittagskaffee sowie Softgetränke an. Sie können selbst an- und abreisen oder alternativ können wir Sie abholen und nach Hause bringen.</p>
  </div>

  <blockquote class="quote">“Ich habe eine Tagespflege gesucht und die neu errichtete Einrichtung von der Sonnhalde GmbH in Lindenau ist echt super. Das Gebäude ist neu, das Personal super und alles klappt bisher echt gut, kann ich nur empfehlen.”<cite>-Frau M</cite></blockquote>

  <p class="claim">Nirgends sonst in der Region erhalten Sie so hochqualitative und zuverlässige Pflege<br>wie bei uns! Wir helfen Ihnen dabei, Ihr Leben einfacher zu gestalten. Rufen Sie uns an!</p>

  <ul class="contacts contacts--left">
    <li><svg width="10" height="10" viewBox="0 0 10 10"><circle cx="5" cy="5" r="5" fill="var(--teal)"/><path d="M3 2.5l1 1.2-.5.8c.4.8.9 1.3 1.7 1.7l.8-.5 1.2 1-.6.8C4.8 7.4 2.7 5.3 2.4 3.1z" fill="#fff"/></svg>Sonnhalde: +49(0) 4100 12 34 50</li>
    <li><svg width="10" height="10" viewBox="0 0 10 10"><circle cx="5" cy="5" r="5" fill="var(--teal)"/><path d="M3 2.5l1 1.2-.5.8c.4.8.9 1.3 1.7 1.7l.8-.5 1.2 1-.6.8C4.8 7.4 2.7 5.3 2.4 3.1z" fill="#fff"/></svg>Lindenau: +49(0)4101 23 45 67 80</li>
    <li><svg width="10" height="10" viewBox="0 0 10 10"><circle cx="5" cy="5" r="5" fill="var(--teal)"/><rect x="2.5" y="3.2" width="5" height="3.6" fill="none" stroke="#fff" stroke-width=".8"/><path d="M2.5 3.2L5 5.2 7.5 3.2" fill="none" stroke="#fff" stroke-width=".8"/></svg>info@pflegeteam-sonnhalde.de</li>
  </ul>
  <div class="contact-divider"></div>
  <ul class="contacts contacts--right">
    <li><svg width="8" height="11" viewBox="0 0 8 11"><path d="M4 0a4 4 0 0 1 4 4c0 3-4 7-4 7S0 7 0 4a4 4 0 0 1 4-4z" fill="var(--teal)"/><circle cx="4" cy="4" r="1.5" fill="var(--black)"/></svg>Birkenweg 12A, Sonnhalde, 24100, Deutschland</li>
    <li><svg width="8" height="11" viewBox="0 0 8 11"><path d="M4 0a4 4 0 0 1 4 4c0 3-4 7-4 7S0 7 0 4a4 4 0 0 1 4-4z" fill="var(--teal)"/><circle cx="4" cy="4" r="1.5" fill="var(--black)"/></svg>Lindenplatz 7, Lindenau,<br>24101, Deutschland</li>
  </ul>
</section>

</body>
</html>
```